New look while maintaining the Brand identification!

I want a new look for my business card. I want to keep the same colors and feel but change the look and layout a bit. The logo (KINOVALEX Physical therapy Reimagined and the lilypad) must remain the same and in that font.
We are a physical therapy clinic. So we have certification that we can write on the back or services we provide (which is what we currently have on the back of the card as well)

Contact information
2846 Cedar Hollow Rd., #22
Naples, FL 34187
P: (239) 555-0172
F: (239) 555-0198
E: kinovalextherapy@example-mail.com
W: www.kinovalextherapy-example.com

Industry/Entity Type

Physical Therapy

Contact Information for Business Card

Our current cards have the business address and information on the back. But I am willing to have it be in the front.

Font styles to use
Sans Serif

Colors
abd036
fbf289
ec1f27

Requirements
Must have
• Has to be unique!
• Services we provide and/or techniques we do must fit on the card
Nice to have
• Would like to have the front and back somehow linked together. Such that if you set the front next to the back, there is a nice flow of design! Currently the back is white with writing on it.
Should not have
• I like the wave lines as compared to straight lines.

```html
<!DOCTYPE html>
<html lang="en">
<head>
<meta charset="utf-8">
<title>KINOVALEX Business Card</title>
<link href="https://fonts.googleapis.com/css2?family=Lato:wght@400;700;900&family=DM+Serif+Display&display=swap" rel="stylesheet">
<style>
  :root {
    --backdrop: #e4e2de;
    --card: #ffffff;
    --card-back: #f7f8f9;
    --lime: #c8d65a;
    --olive: #a9ad3e;
    --gold: #c9b42e;
    --brand: #c2b62c;
    --mark: #abd036;
    --name-green: #b4c23a;
    --red: #ec1f27;
    --ink: #3f4041;
    --muted: #5a5b5c;
    --bullet: #abd036;
  }
  * { margin: 0; padding: 0; box-sizing: border-box; }
  html, body { width: 1200px; height: 1000px; overflow: hidden; }
  body { background: var(--backdrop); font-family: "Lato", sans-serif; position: relative; }

  .card { position: absolute; overflow: hidden; box-shadow: 0 6px 14px rgba(0,0,0,0.18); }
  .card-front { left: 152px; top: 159px; width: 526px; height: 300px; background: var(--card); }
  .card-back { left: 497px; top: 512px; width: 524px; height: 299px; background: var(--card-back); }
  .wave { position: absolute; left: 0; top: 0; }

  .brand-mark { position: absolute; border-radius: 50%; background: var(--mark); }
  .front-mark { left: 157px; top: 72px; width: 22px; height: 22px; }
  .back-mark { left: 411px; top: 204px; width: 26px; height: 26px; }

  .brand-block { position: absolute; left: 32px; top: 98px; text-align: left; }
  .brand-name { font-family: "Lato", sans-serif; font-weight: 900; font-size: 34px; letter-spacing: 0.5px; color: var(--brand); line-height: 1; }
  .brand-tagline { font-family: "Lato", sans-serif; font-weight: 700; font-size: 15px; color: var(--olive); margin-top: 6px; }

  .divider { position: absolute; left: 256px; top: 45px; width: 2px; height: 154px; background: var(--ink); }

  .contact-block { position: absolute; left: 280px; top: 40px; }
  .person-name { font-family: "DM Serif Display", serif; font-size: 24px; color: var(--ink); line-height: 1.1; }
  .person-name .surname { color: var(--name-green); }
  .credentials { font-size: 13.5px; color: var(--muted); margin-top: 3px; margin-bottom: 10px; }
  .contact-list { list-style: none; }
  .contact-list li { display: flex; align-items: flex-start; font-size: 13px; color: var(--ink); line-height: 16px; margin-bottom: 5px; }
  .contact-icon { width: 17px; height: 17px; flex: none; margin-right: 8px; }

  .certifications { position: absolute; left: 0; right: 0; top: 270px; text-align: center; font-size: 13.5px; color: var(--ink); }

  .service-list { position: absolute; list-style: none; }
  .service-list li { position: relative; padding-left: 16px; font-size: 13px; color: var(--ink); line-height: 20.8px; }
  .service-list li::before { content: ""; position: absolute; left: 2px; top: 7px; width: 6px; height: 6px; border-radius: 50%; background: var(--bullet); }
  .services-main { left: 26px; top: 32px; }
  .services-extra { left: 377px; top: 32px; }

  .back-brand { position: absolute; left: 281px; top: 238px; font-family: "Lato", sans-serif; font-weight: 900; font-size: 38px; letter-spacing: 0.5px; color: var(--gold); line-height: 1; }
</style>
</head>
<body>

<section class="card card-front" aria-label="Business card front">
  <svg class="wave" width="526" height="300" viewBox="0 0 526 300" aria-hidden="true">
    <path d="M0,214 C110,190 220,200 320,226 C400,246 470,238 526,228 L526,300 L0,300 Z" fill="var(--olive)"/>
    <path d="M0,222 C110,200 220,212 320,238 C400,256 470,252 526,248 L526,300 L0,300 Z" fill="var(--lime)"/>
  </svg>

  <div class="brand-mark front-mark" aria-hidden="true"></div>
  <div class="brand-block">
    <div class="brand-name">KINOVALEX</div>
    <div class="brand-tagline">Physical Therapy Reimagined</div>
  </div>

  <div class="divider"></div>

  <div class="contact-block">
    <div class="person-name">Dana <span class="surname">Kestrel</span></div>
    <div class="credentials">PT, DPT, MSPT, MBA</div>
    <ul class="contact-list">
      <li>
        <svg class="contact-icon" viewBox="0 0 20 20" aria-hidden="true"><circle cx="10" cy="10" r="10" fill="var(--red)"/><path d="M5,8 Q10,4 15,8 L13.5,9.5 L12,8.5 L8,8.5 L6.5,9.5 Z M6.5,10.5 H13.5 V14 H6.5 Z" fill="#fff"/></svg>
        (239) 555-0172
      </li>
      <li>
        <svg class="contact-icon" viewBox="0 0 20 20" aria-hidden="true"><circle cx="10" cy="10" r="10" fill="var(--red)"/><rect x="7" y="4.5" width="6" height="3.5" fill="#fff"/><rect x="5" y="8" width="10" height="5" rx="1" fill="#fff"/><rect x="7" y="12" width="6" height="3.5" fill="#fff" stroke="var(--red)" stroke-width="0.8"/></svg>
        (239) 555-0198
      </li>
      <li>
        <svg class="contact-icon" viewBox="0 0 20 20" aria-hidden="true"><circle cx="10" cy="10" r="10" fill="var(--red)"/><rect x="5" y="6.5" width="10" height="7" fill="#fff"/><path d="M5,6.5 L10,10.5 L15,6.5" fill="none" stroke="var(--red)" stroke-width="1"/></svg>
        kinovalextherapy@example-mail.com
      </li>
      <li>
        <svg class="contact-icon" viewBox="0 0 20 20" aria-hidden="true"><circle cx="10" cy="10" r="10" fill="var(--red)"/><g fill="none" stroke="#fff" stroke-width="1.1"><circle cx="10" cy="10" r="5"/><ellipse cx="10" cy="10" rx="2.2" ry="5"/><path d="M5,10 H15"/></g></svg>
        www.kinovalextherapy-example.com
      </li>
      <li>
        <svg class="contact-icon" viewBox="0 0 20 20" aria-hidden="true"><circle cx="10" cy="10" r="10" fill="var(--red)"/><path d="M10,15.5 C7,11.5 6,10 6,8.2 A4,4 0 0 1 14,8.2 C14,10 13,11.5 10,15.5 Z" fill="#fff"/><circle cx="10" cy="8.2" r="1.5" fill="var(--red)"/></svg>
        <span>2846 Cedar Hollow Rd., #22<br>Naples, FL 34187</span>
      </li>
    </ul>
  </div>

  <p class="certifications">Certified Halden Scoliosis Therapist . Certified Equine Rehab Specialist. CAPP-OB</p>
</section>

<section class="card card-back" aria-label="Business card back">
  <svg class="wave" width="524" height="299" viewBox="0 0 524 299" aria-hidden="true">
    <path d="M0,218 C90,250 190,238 290,196 C370,162 440,146 524,160 L524,178 C440,162 370,178 290,212 C190,256 90,262 0,224 Z" fill="var(--gold)"/>
  </svg>

  <ul class="service-list services-main">
    <li>Levira Anti-gravity Treadmill</li>
    <li>Class IV Cold Light Laser</li>
    <li>Radial Pulse Shockwave</li>
    <li>Marlo Neurostim</li>
    <li>Veltro Shape</li>
    <li>Granford Technique</li>
    <li>Soft Tissue Oscillator</li>
    <li>Spinal Decompression</li>
  </ul>
  <ul class="service-list services-extra">
    <li>Flexiband Tape</li>
    <li>Steadyfit Wear</li>
    <li>Vestibular Rehab</li>
    <li>Women's Health</li>
  </ul>

  <div class="brand-mark back-mark" aria-hidden="true"></div>
  <div class="back-brand">KINOVALEX</div>
</section>

</body>
</html>
```